ALL TEXT Social Media Graphics

We are looking for a series of social media graphics for Instagram (new size: 4:5 (1080 x 1350 pixels) ratio that are ALL TEXT. We want the following quotes below on each graphic; one quote per graphic. AND, In very small letters at the bottom of each graphic, add @PaulaWrenLive
The look and feel of these graphics should be complimentary to the color palette attached below; but keep them simple. But the design is up to you; at the end of this document, I provided various samples of all text graphics that I like as examples.
The Quotes are in the attached WORD document
women trying to lose weight

```html
<!DOCTYPE html>
<html lang="en">
<head>
<meta charset="utf-8">
<title>All-Text Season Reset Graphics</title>
<link rel="stylesheet" href="https://fonts.googleapis.com/css2?family=Roboto+Condensed:wght@300;700&family=Arimo:wght@400;700&display=swap">
<style>
  :root {
    --pink: #ff0a78;
    --ink: #474747;
    --white: #ffffff;
    --blush: #fdeef3;
    --cream: #f7f3ee;
    --rule: #f48bb8;
  }
  * { margin: 0; padding: 0; box-sizing: border-box; }
  html, body { width: 1200px; height: 581px; overflow: hidden; background: var(--white); }
  .board { position: relative; width: 1200px; height: 581px; }
  .post {
    position: absolute; width: 224.5px; height: 280px;
    background: linear-gradient(160deg, var(--blush) 0%, var(--white) 45%, var(--white) 75%, var(--cream) 100%);
    overflow: hidden;
  }
  .post--plain { background: linear-gradient(180deg, var(--white) 0%, #fbf6f7 100%); }
  .post.c1 { left: 0; } .post.c2 { left: 244px; } .post.c3 { left: 488px; }
  .post.c4 { left: 732px; } .post.c5 { left: 976px; }
  .post.r1 { top: 0; } .post.r2 { top: 301px; }
  .headline {
    position: absolute; font-family: "Roboto Condensed", sans-serif;
    text-transform: uppercase; line-height: 1.08; color: var(--ink); font-weight: 300;
  }
  .headline .hit { color: var(--pink); font-weight: 700; }
  .headline span { display: block; }
  .cta {
    position: absolute; font-family: "Arimo", sans-serif; color: var(--pink);
    font-size: 12px; line-height: 1.6;
  }
  .cta b { font-weight: 700; }
  .cta .program {
    display: inline-block; font-weight: 700;
    border-top: 1px solid var(--rule); border-bottom: 1px solid var(--rule);
    line-height: 1.45; padding: 0 3px; margin-left: -3px;
  }
  .centered { left: 0; right: 0; text-align: center; }
  .centered .program { margin-left: 0; }
  .handle {
    position: absolute; left: 0; bottom: 0; width: 100%; height: 26px;
    background: var(--pink); color: var(--white);
    font-family: "Arimo", sans-serif; font-size: 11.5px;
    display: flex; align-items: center; justify-content: center;
  }
</style>
</head>
<body>
<main class="board">

  <section class="post r1 c1">
    <h2 class="headline" style="left:29px;top:40px;font-size:19px">
      <span class="hit" style="font-size:26px">You can</span>
      <span>absolutely be down</span>
      <span class="hit" style="font-size:26px">20-30 pounds</span>
      <span>by end of summer.</span>
    </h2>
    <p class="cta" style="left:29px;top:147px;font-size:12.5px;line-height:1.65">All it takes is the right<br>planand you've found it.<br>Comment “<b>Glow Up</b>” for the<br><span class="program">Bright Season Reset Plan!</span></p>
    <div class="handle">@PaulaWrenLive</div>
  </section>

  <section class="post post--plain r1 c2">
    <h2 class="headline centered" style="top:31px;font-size:22px">
      <span>You don't need</span>
      <span>another diet</span>
      <span class="hit">—you need a</span>
      <span class="hit">system</span>
      <span class="hit">that works.</span>
    </h2>
    <p class="cta centered" style="top:148px;font-size:11px;line-height:1.45">Drop<br><b style="font-size:14px">30 pounds</b><br>with the<br><span class="program">Bright Season Reset Plan.</span><br>Comment “<b>Summer</b>”<br>to start now.</p>
    <div class="handle">@PaulaWrenLive</div>
  </section>

  <section class="post r1 c3">
    <h2 class="headline" style="left:17px;top:44px;font-size:23px">
      <span>This summer</span>
      <span>ain't over</span>
      <span class="hit">—and neither are</span>
      <span class="hit">your body goals.</span>
    </h2>
    <p class="cta" style="left:20px;top:152px;font-size:13.5px;line-height:1.6">Drop <b>30 pounds</b> with the<br><span class="program">Bright Season Reset Plan.</span><br>Comment “<b>Glow Up</b>”<br>to get the plan.</p>
    <div class="handle">@PaulaWrenLive</div>
  </section>

  <section class="post post--plain r1 c4">
    <h2 class="headline centered" style="top:43px;font-size:20px">
      <span>If your goal is a</span>
      <span>tiny waist, flat belly,</span>
      <span>and</span>
      <span class="hit" style="font-size:24px">30 pounds down</span>
      <span>—this is the plan.</span>
    </h2>
    <p class="cta centered" style="top:161px;font-size:13.5px;line-height:1.4">Comment “<b>Summer</b>”<br>to join the<br><span class="program">Bright Season Reset Plan!</span></p>
    <div class="handle">@PaulaWrenLive</div>
  </section>

  <section class="post r1 c5">
    <h2 class="headline" style="left:27px;top:32px;font-size:23px">
      <span>There's still time</span>
      <span>to drop the</span>
      <span class="hit" style="font-size:22px">30 pounds</span>
      <span>and slay</span>
      <span>this summer.</span>
    </h2>
    <p class="cta" style="left:30px;top:166px;font-size:12.5px;line-height:1.45">The<br><span class="program">Bright Season Reset Plan</span><br>has the blueprint.<br>Comment “<b>Glow Up</b>”!</p>
    <div class="handle">@PaulaWrenLive</div>
  </section>

  <section class="post post--plain r2 c1">
    <h2 class="headline" style="left:26px;top:30px;font-size:25px">
      <span>Snatched waist,</span>
      <span>flat tummy,</span>
      <span class="hit">30 pounds</span>
      <span>lighter</span>
    </h2>
    <p class="cta" style="left:27px;top:152px;font-size:13px;line-height:1.35">&nbsp;— hat's what the<br><span class="program">Bright Season Reset Plan</span><br>Challenge delivers.<br>Comment “<b>Glow Up</b>”<br>to get the plan</p>
    <div class="handle">@PaulaWrenLive</div>
  </section>

  <section class="post r2 c2">
    <h2 class="headline" style="left:24px;top:26px;font-size:25px">
      <span class="hit">Nothing</span>
      <span class="hit">feels better</span>
      <span>than seeing that</span>
      <span>scale drop week</span>
      <span>after week.</span>
    </h2>
    <p class="cta" style="left:24px;top:168px;font-size:12.5px;line-height:1.5">Let's lose up to <b>30 pounds</b><br>this summer—together.<br>Comment “<b>Summer</b>” to join the<br><span class="program">Bright Season Reset Plan!</span></p>
    <div class="handle">@PaulaWrenLive</div>
  </section>

  <section class="post post--plain r2 c3">
    <h2 class="headline centered" style="top:44px;font-size:20.5px;line-height:1.15">
      <span>Sis, we're dropping</span>
      <span>belly flat and</span>
      <span class="hit">saying goodbye</span>
      <span>to stubborn pounds.</span>
    </h2>
    <p class="cta centered" style="top:143px;font-size:14px;line-height:1.55">join the<br><span class="program">Bright Season Reset Plan</span><br>— comment “<b>Summer</b>”!</p>
    <div class="handle">@PaulaWrenLive</div>
  </section>

  <section class="post r2 c4">
    <h2 class="headline" style="left:25px;top:44px;font-size:21px;line-height:1.15">
      <span>Don't wait 'til next</span>
      <span>summer to</span>
      <span>get right.</span>
      <span class="hit" style="font-size:22px">The time is now.</span>
    </h2>
    <p class="cta" style="left:25px;top:152px;font-size:13px;line-height:1.55">Drop <b>30 pounds</b><br>with the<br><span class="program">Bright Season Reset Plan.</span><br>Comment “<b>Summer</b>”!</p>
    <div class="handle">@PaulaWrenLive</div>
  </section>

  <section class="post r2 c5">
    <h2 class="headline" style="left:23px;top:42px;font-size:20px;line-height:1.15">
      <span>You've got</span>
      <span class="hit">8 weeks</span>
      <span>and the perfect plan</span>
      <span>to drop</span>
      <span class="hit">30 pounds.</span>
    </h2>
    <p class="cta" style="left:24px;top:165px;font-size:13px;line-height:1.5">Let's get snatched this<br>summer with the<br><span class="program">Bright Season Reset Plan.</span><br>Comment “<b>Summer</b>”!</p>
    <div class="handle">@PaulaWrenLive</div>
  </section>

</main>
</body>
</html>
```